Alcohol/Drug addiction treatment center and detox facility needs a billboard.

We are a new treatment center in Auburn, IN (2020), specializing in helping folks who are struggling with alcohol/drug addiction. We offer medical detox, inpatient, and outpatient care in a beautiful, safe, and stable environment, where patients will detox comfortably and then learn the coping skills necessary to lead a successful, sober life. The ad should reach people on a personal/emotional level - addicts who are overwhelmed as well as their families - reminding them that the tentacles of addiction are far-reaching; further, it should convey that you are not alone, we are committed to helping you learn how to lead a successful life, and we are here 24/7/365.
Updates

Here are some slogans that are popular in the treatment industry right now: -Your baby’s life shouldn’t begin with 1-866-HEAL-NOW (Maybe use our phone number as the last word) -Treatment Changes Everything. -Brookmere turns fear into Hope. -Pain killers are easy to get into hard to escape -It only takes a little to lose a lot. -Alcohol, Herion, Pills it all kills. -Loved one hooked on Herion? Brookmere ect. -Drive Hammered get nailed -Recovery is real -Brookmere turns fear into hope.

Target Market(s)

People struggling with addiction and their families.

Industry/Entity Type

Addiction Treatment centers

Colors

Designer to choose colors to be used in the design.

Requirements
Must have
• Brookmere Treatment; 866-HEAL-NOW; www.brookmeretreatment.example
Nice to have
• Catchy slogan - Examples: 1. Your baby’s life shouldn’t begin with 1-866-HEAL-Now (we could use our phone number for the last word) 2. Treatment Changes Everything. 3. It only takes a little to lose a lot. 4. Alcohol, Heroin, Pills it all kills. 5. Loved one hooked on Heroin? Brookmere can help. 6. Drive Hammered get nailed 7. Recovery is real 8. Brookmere turns fear into hope. 9. Pain killers are easy to get into hard to escape

```html
<!DOCTYPE html>
<html lang="en">
<head>
<meta charset="utf-8">
<title>Brookmere Treatment Billboard</title>
<link rel="stylesheet" href="https://fonts.googleapis.com/css2?family=Open+Sans:wght@600;700;800&display=swap">
<style>
  :root {
    --navy: #0d2a63;
    --sky: #29b6ea;
    --charcoal: #3a3a3a;
    --white: #ffffff;
    --canvas: #f4f5f7;
    --photo-dark: #2b2620;
    --photo-mid: #6b5443;
    --photo-light: #b9b4ad;
  }
  * { margin: 0; padding: 0; box-sizing: border-box; }
  html, body {
    width: 909px;
    height: 1200px;
    overflow: hidden;
    background: var(--canvas);
  }
  .billboard {
    position: absolute;
    left: 24px;
    top: 475px;
    width: 860px;
    height: 249px;
    background: var(--white);
    box-shadow: 0 6px 18px rgba(0, 0, 0, 0.18);
    font-family: "Open Sans", Arial, sans-serif;
    overflow: hidden;
  }
  .billboard__art {
    position: absolute;
    inset: 0;
  }
  .headline {
    position: absolute;
    left: 268px;
    top: 4px;
    font-size: 86px;
    font-weight: 800;
    line-height: 1;
    letter-spacing: 0.5px;
    color: var(--navy);
  }
  .subhead {
    position: absolute;
    left: 270px;
    top: 86px;
    font-size: 45px;
    font-weight: 800;
    line-height: 1;
    color: var(--charcoal);
    letter-spacing: -0.3px;
  }
  .phone {
    position: absolute;
    left: 286px;
    top: 136px;
    height: 48px;
    display: flex;
    align-items: center;
    gap: 8px;
    color: var(--white);
  }
  .phone__icon { width: 28px; height: 28px; }
  .phone__number {
    font-size: 55px;
    font-weight: 700;
    line-height: 1;
    letter-spacing: -0.5px;
  }
  .brand {
    position: absolute;
    left: 292px;
    top: 205px;
    display: flex;
    align-items: center;
    gap: 7px;
  }
  .brand__dot {
    width: 30px;
    height: 30px;
    border-radius: 50%;
    background: var(--sky);
  }
  .brand__name {
    width: 90px;
    font-size: 12px;
    font-weight: 700;
    line-height: 1.15;
    color: var(--navy);
    text-transform: uppercase;
  }
  .website {
    position: absolute;
    left: 428px;
    top: 207px;
    font-size: 21px;
    font-weight: 700;
    line-height: 1.3;
    color: var(--charcoal);
  }
</style>
</head>
<body>
  <section class="billboard">
    <svg class="billboard__art" width="860" height="249" viewBox="0 0 860 249">
      <defs>
        <linearGradient id="photoTone" x1="0" y1="0" x2="0" y2="1">
          <stop offset="0" stop-color="var(--photo-light)"/>
          <stop offset="0.45" stop-color="var(--photo-mid)"/>
          <stop offset="0.75" stop-color="var(--photo-dark)"/>
          <stop offset="1" stop-color="var(--photo-light)"/>
        </linearGradient>
      </defs>
      <rect class="phone-band" x="240" y="136" width="620" height="48" fill="var(--navy)"/>
      <path class="ring-gap" d="M0 0 H228 A210 210 0 0 1 228 249 H0 Z" fill="var(--white)"/>
      <path class="ring-light" d="M217 -4 A204 204 0 0 1 264 124" fill="none" stroke="var(--sky)" stroke-width="8"/>
      <path class="ring-dark" d="M264 124 A204 204 0 0 1 217 253" fill="none" stroke="var(--navy)" stroke-width="8"/>
      <path class="photo-area" role="img" aria-label="Photo of an overwhelmed man holding his head over a table scattered with pills and syringes"
            d="M0 0 H217 A200 200 0 0 1 217 249 H0 Z" fill="url(#photoTone)"/>
    </svg>

    <h1 class="headline">TREATMENT</h1>
    <p class="subhead">CHANGES EVERYTHING</p>

    <div class="phone">
      <svg class="phone__icon" viewBox="0 0 24 24" aria-hidden="true">
        <path d="M6.6 10.8a15.2 15.2 0 0 0 6.6 6.6l2.2-2.2a1 1 0 0 1 1-.25 11.4 11.4 0 0 0 3.6.57 1 1 0 0 1 1 1V20a1 1 0 0 1-1 1A17 17 0 0 1 3 4a1 1 0 0 1 1-1h3.5a1 1 0 0 1 1 1 11.4 11.4 0 0 0 .57 3.6 1 1 0 0 1-.25 1z" fill="var(--sky)"/>
        <path d="M14 3.5a6.5 6.5 0 0 1 6.5 6.5M14 7a3 3 0 0 1 3 3" fill="none" stroke="var(--sky)" stroke-width="1.8" stroke-linecap="round"/>
      </svg>
      <span class="phone__number">1-866-HEAL-NOW</span>
    </div>

    <div class="brand">
      <span class="brand__dot"></span>
      <span class="brand__name">Brookmere Treatment</span>
    </div>
    <p class="website">www.brookmeretreatment.example</p>
  </section>
</body>
</html>
```